Design a Website in Wordpress for an Australian Health Training Company in Health related courses

We require a WORDPRESS based Website (due to add on's we need to use for third party software) to replace our old site.
We offer national face to face delivery in medical reception, terminology and also administration.
The website will have around 6 pages and the ability to describe our main 6 courses (perhaps on the Courses page this may be tabs opening up to details for example?)
I have attached a previous sample of a Joomla site which was being developed (please do not feel you have to copy this - but I am just giving it as a sample - copying would be boring). But it gives an idea of look/feel and colours which may be suitable. Open to other ideas though.
I will provide some of the content, but would like the ability to finish the content myself.
Images and graphics are important. While a few medical photos re great - don't be tempted to us all pictures of doctors and nurses (although a couple would be good) - these are administrative courses so general corporate, eye catching visionary pictures of people in general are great. A medical type picture is also fine.
THE BOOKING system - will be via an ADD ON which will occur at the end of the project and is supplied by a third party software company (our student management system). This project will include up to 2 hours working with the Tech guys from the third party software to enable the ADD ON. If this ADD ON requires more time, we will pay hourly (although I do not expect it will).
Mostly a female market, many mature aged women target 25-45 yrs. Mixture of medical/health and corporate. Maybe a bit of mums returning to work and corporate inspiration.
It Company
Coded - Design and coding required
5+ page
Must have
- Wordpress
- Great graphics
- Interesting
- professional and clean
- Enquiry section (info Pak)
- Should have a University feel to it - Education
- Pages
- Home Page - About Us - Recruitment -Courses - Class Schedule - Traineeships Queensland Funding - Latest News Blog - Corporate Training- Contact us

```html
<!DOCTYPE html>
<html lang="en">
<head>
<meta charset="utf-8">
<title>Kestrel – Courses for Busy People</title>
<link href="https://fonts.googleapis.com/css2?family=Roboto:wght@300;400;500;700&family=Great+Vibes&display=swap" rel="stylesheet">
<style>
:root{
  --blue:#1a56a8;
  --blue-dark:#12448a;
  --ink:#333;
  --muted:#666;
  --light:#f1f2f4;
  --card:#e4e5e7;
  --footer:#2f3237;
  --footer-deep:#26282c;
  --footer-text:#9aa0a6;
  --white:#fff;
}
*{box-sizing:border-box;margin:0;padding:0}
html,body{width:1200px;height:3358px;overflow:hidden}
body{font-family:"Roboto",Arial,sans-serif;color:var(--ink);background:var(--white);position:relative}
.abs{position:absolute}
/* top bar */
.topbar{left:0;top:0;width:1200px;height:32px;background:var(--light);font-size:12px;color:var(--muted)}
.topbar .links{left:52px;top:9px;display:flex;gap:28px}
.topbar .util{right:52px;top:9px;display:flex;gap:26px;align-items:center}
.flag{display:inline-block;width:16px;height:10px;background:#3a4fa0;margin-right:5px;vertical-align:-1px}
/* header */
.header{left:0;top:32px;width:1200px;height:76px;background:var(--white)}
.brand{left:72px;top:24px;display:flex;align-items:center;gap:8px;font-size:15px;font-weight:700;color:var(--blue)}
.brand .mark{width:20px;height:20px;background:var(--blue);border-radius:50%}
.nav{right:52px;top:28px;display:flex;gap:34px;font-size:14px;color:#222}
/* hero */
.hero{left:0;top:108px;width:1200px;height:546px;background:linear-gradient(115deg,#8fa7b8 0%,#c7b49d 40%,#d9b89a 60%,#8d6f5a 100%)}
.hero-shade{left:0;top:0;width:1200px;height:546px;background:rgba(20,25,35,.35)}
.hero h1{left:0;top:130px;width:1200px;text-align:center;font-family:"Great Vibes",cursive;font-weight:400;font-size:84px;color:var(--white);letter-spacing:2px}
.hero p{left:170px;top:244px;width:860px;text-align:center;font-size:21px;line-height:32px;color:var(--white)}
.hero .btns{left:0;top:336px;width:1200px;display:flex;justify-content:center;gap:40px}
.btn-ghost{padding:10px 18px;font-size:11px;font-weight:700;color:var(--ink);background:var(--white);border:1px solid #ddd}
.dots{left:0;top:508px;width:1200px;display:flex;justify-content:center;gap:10px}
.dots i{width:9px;height:9px;border-radius:50%;background:rgba(255,255,255,.6)}
.dots i.on{background:var(--white)}
/* like bar */
.likebar{left:376px;top:672px;width:448px;height:38px;border:1px solid #ddd;border-radius:20px;display:flex;align-items:center;gap:12px;padding-left:14px;font-size:11px;color:var(--muted);background:var(--white)}
.likebar .sep{width:1px;height:38px;background:#ddd}
.likebar .chip{width:42px;height:16px;background:#5a71a8;border-radius:2px}
.rule{left:52px;width:1096px;border-top:2px dotted var(--blue)}
.sec-title{left:0;width:1200px;text-align:center;font-size:24px;font-weight:700;color:var(--blue)}
/* intro */
.intro{left:100px;top:826px;width:1000px;text-align:center;font-size:12px;line-height:20px;color:#444}
.intro p{margin-bottom:17px}
/* courses */
.courses{left:0;top:1108px;width:1200px;height:305px;background:var(--light)}
.course{top:112px;width:168px;height:180px;background:var(--card)}
.course .ico{left:38px;top:-24px;width:92px;height:92px;border-radius:50%;background:var(--blue);border:5px solid var(--white);display:flex;align-items:center;justify-content:center}
.course h3{left:8px;top:84px;width:152px;text-align:center;font-size:16px;line-height:22px;font-weight:500;color:#222}
/* promo band */
.promo{left:0;top:1413px;width:1200px;height:166px;background:var(--blue)}
.promo h2{left:52px;top:48px;width:880px;font-size:28px;line-height:37px;font-weight:400;color:var(--white)}
.promo .book{left:986px;top:60px;padding:14px 28px;background:var(--white);color:var(--blue);font-size:13px;font-weight:700}
/* features */
.features{left:0;top:1579px;width:1200px;height:387px;background:linear-gradient(180deg,#4a5058,#3a3f46 60%,#2e3238)}
.features .shade{left:0;top:0;width:1200px;height:387px;background:rgba(0,0,0,.35)}
.feat{top:52px;width:210px;text-align:center;color:var(--white)}
.feat .ico{margin:0 auto;width:86px;height:86px;border-radius:50%;background:var(--blue);display:flex;align-items:center;justify-content:center}
.feat .ico.value{background:var(--white);border:5px solid var(--blue)}
.feat h3{margin-top:24px;font-size:18px;font-weight:500}
.feat h3.hl{color:var(--blue)}
.feat p{margin-top:12px;font-size:12px;line-height:17px}
/* testimonials */
.quote{width:520px;font-size:12px;line-height:17px;font-style:italic;color:#444}
.quote.right{text-align:left}
.quote.left{text-align:right}
.quote .who{margin-top:12px;font-style:normal;font-size:12px;color:#222}
.avatar{width:76px;height:76px;border-radius:50%;background:linear-gradient(135deg,#d7b9a3,#8a6a58)}
.vdiv{left:599px;top:2050px;height:346px;border-left:2px dotted #aab}
.hdiv{left:80px;top:2210px;width:1040px;border-top:2px dotted #aab}
/* posts */
.post{top:2497px;width:252px;height:358px;background:var(--light)}
.post .img{left:0;top:0;width:252px;height:191px}
.post h3{left:20px;top:212px;font-size:18px;font-weight:500;color:#222}
.post p{left:20px;top:244px;width:212px;font-size:13px;line-height:19px;color:var(--muted)}
.post .meta{left:20px;top:322px;width:212px;display:flex;justify-content:space-between;font-size:10px;color:var(--muted)}
.more{left:536px;top:2893px;width:128px;height:40px;background:var(--blue);color:var(--white);font-size:12px;font-weight:700;text-align:center;line-height:40px}
/* footer */
.footer{left:0;top:2947px;width:1200px;height:368px;background:var(--footer)}
.fcol{top:34px;width:240px;color:var(--footer-text);font-size:12.5px;line-height:20px}
.fcol h4{color:var(--white);font-size:17px;font-weight:500;margin-bottom:22px}
.fpost{display:flex;gap:14px;align-items:center;margin-bottom:20px}
.fpost .th{width:42px;height:42px;border-radius:50%;background:#5a5e64;flex:none}
.fpost b{display:block;color:var(--white);font-weight:400;font-size:12.5px}
.fpost small{font-size:10px}
.social{display:flex;gap:14px;margin-top:20px}
.social i{width:11px;height:11px;border-radius:50%;background:var(--footer-text)}
.copy{left:0;top:3315px;width:1200px;height:43px;background:var(--footer-deep);color:var(--footer-text);font-size:11px;padding:16px 52px}
</style>
</head>
<body>

<div class="abs topbar">
  <div class="abs links"><span>Home</span><span>About Us</span><span>Blog</span><span>Contact us</span></div>
  <div class="abs util"><span><span class="flag"></span>English ⌄</span><span>Login/Register</span>
    <svg width="12" height="12" viewBox="0 0 12 12"><circle cx="5" cy="5" r="3.8" fill="none" stroke="#555" stroke-width="1.5"/><line x1="8" y1="8" x2="11" y2="11" stroke="#555" stroke-width="1.5"/></svg></div>
</div>

<header class="abs header">
  <div class="abs brand"><span class="mark"></span>Kestrel</div>
  <nav class="abs nav"><span>Recruitment</span><span>Courses</span><span>Class Schedule</span><span>Traineeships Queensland</span><span>Funding</span><span>Corporate Training</span></nav>
</header>

<section class="abs hero" role="img" aria-label="Photo of smiling women in a bright classroom">
  <div class="abs hero-shade"></div>
  <h1 class="abs">Courses for Busy People</h1>
  <p class="abs">Our unique paceLAB(Combined Assesment &amp; Training) class format delivers accelerated training that's specifically targeted at busy profes-sionals</p>
  <div class="abs btns"><span class="btn-ghost">READ MORE</span><span class="btn-ghost">GO ON SURFING</span></div>
  <div class="abs dots"><i class="on"></i><i></i><i class="on"></i></div>
</section>

<div class="abs rule" style="top:690px;width:320px"></div>
<div class="abs rule" style="top:690px;left:828px;width:320px"></div>
<div class="abs likebar">
  <svg width="16" height="16" viewBox="0 0 16 16"><path d="M2 7h3v8H2zM6 7l3-6c1.5 0 2 1 2 2l-.5 3H15l-1 8H6z" fill="none" stroke="#bbb" stroke-width="1.2"/></svg>
  <span class="sep"></span><span class="chip"></span><span>You and 4.1k others like this.</span>
</div>

<h2 class="abs sec-title" style="top:734px">Intro</h2>
<div class="abs rule" style="top:772px"></div>
<div class="abs intro">
  <p>Kestrel is Australia's Leading Provider of Educational, Training and Support Services for the Medical and Dental industry - enabling students to be immediately skilled and 'Job Ready' for a career in Health.</p>
  <p>Kestrel is a Registered Training Organisation offering specialised Medical Administration Training in over 15 locations Australia wide. Kestrel have trained thousands of students the required knowledge and skills to become successful health care administrators.</p>
  <p>Our unique Short Medical Reception and Terminology Course and our Full Qualification is Nationally Accredited and the go-to recognised qualification in industry.</p>
  <p>Did you know that Kestrel has been operating in Australia for over 16 years! During this time, Kestrel have developed a reputation second to none for training highly sought after medical receptionists, secretaries and administrators.</p>
  <p>Our course material and unique training programme is developed in conjunction with Industry to reflect the latest requirements in health administration. Kestrel also believe understanding the medical culture is as important as good skills. Our team of specialised trainers are both experienced in industry and also hold special qualifications in adult education and are fully accredited.</p>
</div>

<section class="abs courses">
  <h2 class="abs sec-title" style="top:12px">List of Courses</h2>
  <div class="abs rule" style="top:50px"></div>
  <div class="abs course" style="left:42px"><div class="abs ico"><svg width="40" height="40" viewBox="0 0 40 40" fill="none" stroke="#fff" stroke-width="2"><rect x="8" y="14" width="24" height="20"/><path d="M4 14L20 5l16 9"/><rect x="16" y="24" width="8" height="10"/><path d="M20 15v5M17.5 17.5h5"/></svg></div><h3 class="abs">Medical Reception &amp; Terminology</h3></div>
  <div class="abs course" style="left:234px"><div class="abs ico"><svg width="40" height="40" viewBox="0 0 40 40" fill="none" stroke="#fff" stroke-width="2"><circle cx="20" cy="9" r="4"/><path d="M13 36V19h14v17M20 19v17"/><circle cx="20" cy="20" r="17"/></svg></div><h3 class="abs">Cert III Business Administration (Medical)</h3></div>
  <div class="abs course" style="left:426px"><div class="abs ico"><svg width="40" height="40" viewBox="0 0 40 40" fill="none" stroke="#fff" stroke-width="2"><circle cx="20" cy="20" r="4"/><circle cx="8" cy="8" r="3"/><circle cx="32" cy="8" r="3"/><circle cx="8" cy="32" r="3"/><circle cx="32" cy="32" r="3"/><path d="M10 10l7 7M30 10l-7 7M10 30l7-7M30 30l-7-7"/></svg></div><h3 class="abs">Medical Terminology</h3></div>
  <div class="abs course" style="left:618px"><div class="abs ico"><svg width="40" height="40" viewBox="0 0 40 40" fill="none" stroke="#fff" stroke-width="2"><rect x="4" y="11" width="32" height="19" rx="2"/><path d="M9 16h2M14 16h2M19 16h2M24 16h2M29 16h2M9 21h2M14 21h2M19 21h2M24 21h2M29 21h2M12 26h16"/></svg></div><h3 class="abs">Keyboard and Typing</h3></div>
  <div class="abs course" style="left:810px"><div class="abs ico"><svg width="40" height="40" viewBox="0 0 40 40" fill="none" stroke="#fff" stroke-width="2"><rect x="6" y="6" width="28" height="28" rx="3"/><circle cx="20" cy="17" r="5"/><path d="M11 31c2-6 16-6 18 0"/></svg></div><h3 class="abs">Kestrel Online</h3></div>
  <div class="abs course" style="left:1002px"><div class="abs ico"><svg width="40" height="40" viewBox="0 0 40 40" fill="none" stroke="#fff" stroke-width="2"><rect x="9" y="4" width="24" height="32" rx="2"/><path d="M6 10h6M6 17h6M6 24h6M6 31h6M16 12h12M16 18h12M16 24h8"/></svg></div><h3 class="abs">Confidentiality</h3></div>
</section>

<section class="abs promo">
  <h2 class="abs">Enrol in our new BSB51915 Diploma of Leadership and Management and gain valuable skills to launch your managemnt career</h2>
  <span class="abs book">BOOKING NOW!</span>
</section>

<section class="abs features" role="img" aria-label="Dimmed photo of a modern office interior">
  <div class="abs shade"></div>
  <div class="abs feat" style="left:44px"><div class="ico"><svg width="38" height="38" viewBox="0 0 16 16"><path d="M2 7h3v8H2zM6 7l3-6c1.5 0 2 1 2 2l-.5 3H15l-1 8H6z" fill="none" stroke="#fff" stroke-width="1.2"/></svg></div><h3>Quality</h3><p>Kestrel delivery quality, effective training facilitated by industry leaders. Just ask our students who rate us an average of 4.7 out of 5.</p></div>
  <div class="abs feat" style="left:269px"><div class="ico"><svg width="38" height="38" viewBox="0 0 40 40" fill="#fff"><path d="M34 6c-10 0-17 6-20 14l6 6c8-3 14-10 14-20zM12 22l-6 2 4-8h6zM18 28l-2 6 8-4v-6zM10 26l4 4-8 4z"/></svg></div><h3>Experience</h3><p>Kestrel is Australia's largest and leading provider of nationally recognised training in health administration – training from over 17 locations Australia wide.</p></div>
  <div class="abs feat" style="left:495px"><div class="ico value"><svg width="40" height="40" viewBox="0 0 40 40"><circle cx="20" cy="20" r="16" fill="var(--blue)"/><circle cx="20" cy="20" r="11" fill="none" stroke="#fff" stroke-width="2"/><text x="20" y="25" text-anchor="middle" font-size="14" font-weight="700" fill="#fff" font-family="Roboto,sans-serif">$</text></svg></div><h3 class="hl">Value</h3><p>Our innovative teaching approach allows us to deliver exceptional training at affordable prices with no hidden extras.</p></div>
  <div class="abs feat" style="left:721px"><div class="ico"><svg width="40" height="40" viewBox="0 0 40 40" fill="none" stroke="#fff" stroke-width="2.2"><path d="M4 16l8-6 8 4 8-4 8 6-12 12c-2 2-4 2-6 0z"/><path d="M14 22l4 4M18 20l4 4"/></svg></div><h3>Industry Recognised</h3><p>Kestrel work hand in hand with industry to develop our core programme and consolidate the programme annually to keep the programme fresh and relevant.</p></div>
  <div class="abs feat" style="left:946px"><div class="ico"><svg width="38" height="38" viewBox="0 0 40 40" fill="#fff"><path d="M11 5h18v10a9 9 0 0 1-18 0zM17 24h6v6h-6zM12 31h16v4H12z"/><path d="M11 8H5c0 6 3 9 7 9M29 8h6c0 6-3 9-7 9" fill="none" stroke="#fff" stroke-width="2"/></svg></div><h3>Great Job Results</h3><p>Kestrel students get jobs! Our focus is to create job-ready students who are mentored to achieve their goals. Kestrel also provide a recruitment service for industry and graduates.</p></div>
</section>

<h2 class="abs sec-title" style="top:1978px">What People Say</h2>
<div class="abs rule" style="top:2018px"></div>
<div class="abs vdiv"></div>
<div class="abs hdiv"></div>

<div class="abs quote left" style="left:62px;top:2078px;width:420px">"I want to say a huge thank you for the course and knowledge I came away with. I have secured a fantastic job after my first application! Such good value for money too! I would highly recommend it. I'm a mature aged person so it's never too late to up -skill yourself to get what you deserve!<div class="who">Mara Lind</div></div>
<div class="abs avatar" style="left:494px;top:2080px" role="img" aria-label="Portrait photo of a student"></div>
<div class="abs avatar" style="left:632px;top:2080px" role="img" aria-label="Portrait photo of a student"></div>
<div class="abs quote right" style="left:740px;top:2078px;width:400px">"I have just completed my 6 month probation period at Brookvale Hospital and loving it. It was my first medical job I applied for literally 1-2 weeks after I finished the course. Thanks to you, Lena, and all the other teachers and staff at Kestrel Health Management."<div class="who">Tessa</div></div>

<div class="abs quote left" style="left:62px;top:2238px;width:420px">I completed your Medical Receptionist course over a year ago. It was the best experience by far. I got a job 2 months after completing this course as a receptionist at a Neuro Physiotherapy practice. I have been with the practice little over a year and I am now the practice administrator. I love my job, I love the people I work with and I love going to work every day!<div class="who">Nadia</div></div>
<div class="abs avatar" style="left:494px;top:2236px" role="img" aria-label="Portrait photo of a student"></div>
<div class="abs avatar" style="left:632px;top:2236px" role="img" aria-label="Portrait photo of a student"></div>
<div class="abs quote right" style="left:740px;top:2238px;width:400px">I started my working career in childcare. I always knew I am capable of more all I needed was the Kestrel course – and to have faith in myself. My message to your future students is; believe in yourselves and everything will fall into place it doesn't matter if you're loud or quiet, shy or confident. I love my new position as a medical receptionist and I have never looked back!<div class="who">Robin</div></div>

<h2 class="abs sec-title" style="top:2402px">Recent Posts</h2>
<div class="abs rule" style="top:2442px"></div>

<article class="abs post" style="left:52px"><div class="abs img" role="img" aria-label="Photo of a traveller with a leather bag" style="background:linear-gradient(160deg,#6b4a33,#a67a52 60%,#3e2c22)"></div><h3 class="abs">Standard Post</h3><p class="abs">Enim congue blandit. Lorem ipsum dolor sit amet, consectetur adipiscing elit. Quisque...</p><div class="abs meta"><span>▦ 22 June, 2015</span><span>● 0</span></div></article>
<article class="abs post" style="left:334px"><div class="abs img" role="img" aria-label="Video still of a dim interior" style="background:linear-gradient(160deg,#2e3a44,#4c5a66)"><svg class="abs" style="left:112px;top:82px" width="28" height="28"><rect width="28" height="28" fill="#1a56a8"/><path d="M10 9l9 5-9 5z" fill="#fff"/></svg></div><h3 class="abs">Video Post</h3><p class="abs">Ultrices posuere cubilia curae curabitur sit amet tortor ut massa commodo. Vestibulum...</p><div class="abs meta"><span>▦ 22 June, 2015</span><span>● 0</span></div></article>
<article class="abs post" style="left:614px"><div class="abs img" role="img" aria-label="Photo of a café with a brick wall" style="background:linear-gradient(160deg,#8a5a3c,#c49a70 55%,#5c3e2c)"></div><h3 class="abs">Post with Image</h3><p class="abs">Enim congue blandit. Lorem ipsum dolor sit amet, consectetur adipiscing elit. Quisque...</p><div class="abs meta"><span>▦ 22 June, 2015</span><span>● 0</span></div></article>
<article class="abs post" style="left:896px"><div class="abs img" role="img" aria-label="Photo of an old wallet with banknotes" style="background:linear-gradient(160deg,#e6dccb,#b08460 60%,#6e4b34)"></div><h3 class="abs">Image Post</h3><p class="abs">Ultrices posuere cubilia curae curabitur sit amet tortor ut massa commodo. Vestibulum...</p><div class="abs meta"><span>▦ 22 June, 2015</span><span>● 0</span></div></article>

<span class="abs more">VIEW MORE</span>

<footer class="abs footer">
  <div class="abs fcol" style="left:52px"><h4>About</h4><p>Maecenas etos sit amet, consectetur adipiscing elit. Terminal volutpat rutrum metro amet sollicitudin interdum. Maecenas etos sit amet, consectetur adipiscing elit. Terminal volutpat rutrum metro amet sollicitudin interdum. Maecenas etos sit amet, consectetur adipiscing elit. Terminal volutpat rutrum metro amet sollicitudin interdum.</p><div class="social"><i></i><i></i><i></i><i></i><i></i></div></div>
  <div class="abs fcol" style="left:332px"><h4>Recent Posts</h4>
    <div class="fpost"><span class="th"></span><span><b>Business Cards Design Trends</b><small>Dec 02, 2020 / 2 comments</small></span></div>
    <div class="fpost"><span class="th"></span><span><b>This Maravelous App</b><small>Nov 18, 2020 / 6 comments</small></span></div>
    <div class="fpost"><span class="th"></span><span><b>Brand Paper Niceties</b><small>Nov 10, 2020 / 0 comments</small></span></div>
  </div>
  <div class="abs fcol" style="left:614px"><h4>Latest Twitts</h4></div>
  <div class="abs fcol" style="left:894px"><h4>Contact Us</h4><p>Maecenas etos sit amet, consectetur adipiscing elit. Terminal volutpat rutrum metro amet sollicitudin interdum.</p>
    <p style="margin-top:16px">Phone: +1 (800) 555 01 42</p><p style="margin-top:10px">Office: 418 Harlow Street, Newbury</p><p style="margin-top:10px">Email: info@lumora.com</p></div>
</footer>
<div class="abs copy">Copyright 2020. All Rights Reserved by Lumora.</div>

</body>
</html>
```